Sales Presentation Powerpoint

This project is to design a sales presentation for a new service/product for hotels.
The product is called snug stay and is a tablet pc that we propose to install in hotel rooms free of charge to hotels. The system has information about the hotel, room service menus, entertainment such as games, web browser, and other functions.
Marketing material has already been designed and the sell sheet that was recently completed is attached for your use.

Additionally, you will need to visit www.snugstaypad.example to see a demo of the product.

PRESENTATION REQUIRMENTS
General requirements – We will select the presentation that is the most visually crisp and stunning, stays within our already established visual themes, and includes multimedia. Interactivity and movement is a big plus if you can incorporate it into the presentation. We will be recording voiceover work on the presentation after it is made so you can plan around that thought.

PRESENTATION FLOW
1. General introduction to the product and what it is (info found on the sell sheet or you can contact me for more details if needed.
2. advantages of the product. Info found on the sell sheet or you can contact me for more details. Each of the main points on the sell sheet need to be a separate slide though so we can speak to it.
3. walkthrough of the product. I would like an animation, screen shots, or something similar to give the view the chance to experience and see the software. The demo at www.snugstaypad.example is the best place to go for that.

Recommendation for design:
Can we have the presentation be framed in a tablet window. to clarify, the border around the presentation is a tablet pc and the presentation appears inside of that.

Tools:
please feel free to use any software. does not need to be powerpoint. if you feel comfortable with solutions such as slidora, deckwave, or any other system you may use that.
Updates

Target Market(s)

presentation is for potential customers

Industry/Entity Type

Entertainment

Requirements
Must have
• visually crisp, sharp, and stunning
adheres to already established style from sell sheet and website.
multimedia encorporation a big plus.

```html
<!DOCTYPE html>
<html lang="en">
<head>
<meta charset="utf-8">
<title>Snug Stay – Why Snug Stay</title>
<link href="https://fonts.googleapis.com/css2?family=Arimo:wght@400;700&display=swap" rel="stylesheet">
<style>
  :root {
    --brand-red: #8b0306;
    --brand-red-dark: #840206;
    --brand-red-light: #930509;
    --bullet-red: #a0080c;
    --panel-grey: #e7eaed;
    --panel-grey-light: #eef0f2;
    --text-dark: #111111;
    --text-muted: #a8a8a8;
    --rule-grey: #c9c9c9;
    --white: #ffffff;
  }
  * { margin: 0; padding: 0; box-sizing: border-box; }
  html, body { width: 1200px; height: 900px; overflow: hidden; background: var(--white); }
  body { font-family: "Arimo", Arial, sans-serif; }

  .slide { position: relative; width: 1200px; height: 900px; background: var(--white); }

  .slide-header {
    position: absolute; left: 0; top: 0; width: 1200px; height: 130px;
    background: linear-gradient(180deg, var(--brand-red-dark) 0%, var(--brand-red) 55%, var(--brand-red-light) 100%);
  }
  .slide-title {
    position: absolute; left: 59px; top: 72px;
    color: var(--white); font-weight: 700; font-size: 41px; letter-spacing: 0.3px; line-height: 1;
  }

  .content-panel {
    position: absolute; left: 0; top: 130px; width: 1200px; height: 608px;
    background: linear-gradient(180deg, var(--panel-grey) 0%, var(--panel-grey-light) 100%);
  }
  .benefit-list { list-style: none; position: absolute; left: 60px; top: 40px; }
  .benefit-item {
    display: flex; align-items: center; height: 56.2px;
    font-size: 24px; color: var(--text-dark); white-space: nowrap;
  }
  .bullet-icon { width: 14px; height: 16px; margin-right: 29px; flex: none; }

  .footer-band {
    position: absolute; left: 0; top: 738px; width: 1200px; height: 15px; background: var(--brand-red);
  }
  .footer-rule {
    position: absolute; left: 0; top: 753px; width: 1200px; height: 4px;
    background: linear-gradient(180deg, var(--rule-grey), var(--white));
  }
  .copyright {
    position: absolute; left: 29px; top: 816px;
    font-size: 24px; color: var(--text-muted);
  }
  .brand-mark {
    position: absolute; left: 1052px; top: 810px;
    display: flex; align-items: center; gap: 8px;
  }
  .brand-dot { width: 26px; height: 26px; border-radius: 50%; background: var(--brand-red); }
  .brand-name { font-size: 17px; font-weight: 700; color: var(--text-dark); }
</style>
</head>
<body>
<main class="slide">
  <header class="slide-header">
    <h1 class="slide-title">WHY SNUG STAY</h1>
  </header>

  <section class="content-panel">
    <ul class="benefit-list">
      <li class="benefit-item"><svg class="bullet-icon" viewBox="0 0 14 16"><path d="M3 2 L10 8 L3 14" fill="none" stroke="#a0080c" stroke-width="3.5"/></svg>In-room tablets installed free of charge to your hotel</li>
      <li class="benefit-item"><svg class="bullet-icon" viewBox="0 0 14 16"><path d="M3 2 L10 8 L3 14" fill="none" stroke="#a0080c" stroke-width="3.5"/></svg>Hotel information and services at every guest's fingertips</li>
      <li class="benefit-item"><svg class="bullet-icon" viewBox="0 0 14 16"><path d="M3 2 L10 8 L3 14" fill="none" stroke="#a0080c" stroke-width="3.5"/></svg>Room service menus browsed and ordered from the bed</li>
      <li class="benefit-item"><svg class="bullet-icon" viewBox="0 0 14 16"><path d="M3 2 L10 8 L3 14" fill="none" stroke="#a0080c" stroke-width="3.5"/></svg>Games and entertainment for guests of every age group</li>
      <li class="benefit-item"><svg class="bullet-icon" viewBox="0 0 14 16"><path d="M3 2 L10 8 L3 14" fill="none" stroke="#a0080c" stroke-width="3.5"/></svg>A full web browser for news, email and local city guides</li>
      <li class="benefit-item"><svg class="bullet-icon" viewBox="0 0 14 16"><path d="M3 2 L10 8 L3 14" fill="none" stroke="#a0080c" stroke-width="3.5"/></svg>New revenue from promotions, upsells and guest offers</li>
    </ul>
  </section>

  <div class="footer-band"></div>
  <div class="footer-rule"></div>

  <footer>
    <p class="copyright">Copyright @ 2012</p>
    <div class="brand-mark">
      <span class="brand-dot"></span>
      <span class="brand-name">Snug Stay</span>
    </div>
  </footer>
</main>
</body>
</html>
```